Design a New Business Card for Our Company

We are looking for fresh, unique, and a modern business card that reflects our roots as digital marketing agency focused on SEM.

Industry/Entity Type

Marketing

Contact Information for Business Card

looking for very unique out of the box designs. clean and modern that compliments our logo

Requirements
Must have
• colors should match our logo
• Front should have name, address, email, and phone/fax of the person, phone/fax are the same number
• back should have our url

```html
<!DOCTYPE html>
<html lang="en">
<head>
<meta charset="utf-8">
<title>Brightpath Media – Business Cards</title>
<link href="https://fonts.googleapis.com/css2?family=Josefin+Sans:wght@300;700&family=Lobster&display=swap" rel="stylesheet">
<style>
  :root {
    --stage: #e6e6e4;
    --card-green: #b5bd3a;
    --band-blue: #6498cf;
    --logo-grey: #bdb8b1;
    --ink-white: #ffffff;
  }
  html, body {
    margin: 0;
    padding: 0;
    width: 1200px;
    height: 799px;
    overflow: hidden;
    background: var(--stage);
  }
  .stage {
    position: relative;
    width: 1200px;
    height: 799px;
    display: flex;
    align-items: center;
    justify-content: center;
    gap: 60px;
  }
  .card {
    position: relative;
    width: 500px;
    height: 286px;
    background: var(--card-green);
    box-shadow: 0 6px 18px rgba(0,0,0,0.18);
    overflow: hidden;
    font-family: "Josefin Sans", sans-serif;
  }
  .brand {
    position: absolute;
    display: flex;
    align-items: center;
    gap: 14px;
  }
  .brand-dot {
    width: 46px;
    height: 46px;
    border-radius: 50%;
    background: var(--logo-grey);
    flex: none;
  }
  .brand-name {
    font-family: "Josefin Sans", sans-serif;
    font-weight: 700;
    font-size: 42px;
    line-height: 1;
    color: var(--logo-grey);
    white-space: nowrap;
    padding-top: 6px;
  }
  .card-back .brand { left: 78px; top: 82px; }
  .card-front .brand { left: 48px; top: 62px; }
  .band {
    position: absolute;
    left: 0;
    right: 0;
    bottom: 0;
    height: 66px;
    background: var(--band-blue);
    display: flex;
    align-items: center;
    color: var(--ink-white);
    font-weight: 300;
  }
  .band-back {
    padding-left: 40px;
    gap: 18px;
    font-size: 21px;
  }
  .band-front {
    justify-content: space-between;
    padding: 0 20px;
    font-size: 11.5px;
    letter-spacing: 0.02em;
  }
  .contact {
    display: flex;
    align-items: center;
    gap: 7px;
    white-space: nowrap;
  }
  .contact svg { flex: none; }
  .person-name {
    position: absolute;
    right: 54px;
    top: 128px;
    font-family: "Lobster", cursive;
    font-size: 30px;
    color: var(--ink-white);
  }
</style>
</head>
<body>
<main class="stage">

  <section class="card card-back" aria-label="Card back">
    <div class="brand">
      <span class="brand-dot"></span>
      <span class="brand-name">Brightpath Media</span>
    </div>
    <div class="band band-back">
      <svg width="40" height="40" viewBox="0 0 40 40" aria-hidden="true">
        <circle cx="20" cy="20" r="18" fill="none" stroke="#fff" stroke-width="2.5"/>
        <ellipse cx="20" cy="20" rx="8" ry="18" fill="none" stroke="#fff" stroke-width="2"/>
        <line x1="20" y1="2" x2="20" y2="38" stroke="#fff" stroke-width="2"/>
        <line x1="2" y1="20" x2="38" y2="20" stroke="#fff" stroke-width="2"/>
        <line x1="5" y1="12" x2="35" y2="12" stroke="#fff" stroke-width="2"/>
        <line x1="5" y1="28" x2="35" y2="28" stroke="#fff" stroke-width="2"/>
      </svg>
      <span class="url">www.brightpathmedia.com</span>
    </div>
  </section>

  <section class="card card-front" aria-label="Card front">
    <div class="brand">
      <span class="brand-dot"></span>
      <span class="brand-name">Brightpath Media</span>
    </div>
    <p class="person-name" style="margin:0">Full Name</p>
    <div class="band band-front">
      <span class="contact">
        <svg width="18" height="22" viewBox="0 0 18 22" aria-hidden="true">
          <path d="M9 1a7 7 0 0 0-7 7c0 5 7 13 7 13s7-8 7-13a7 7 0 0 0-7-7z" fill="#fff"/>
          <circle cx="9" cy="8" r="2.6" fill="#6498cf"/>
        </svg>
        Current Address
      </span>
      <span class="contact">
        <svg width="22" height="16" viewBox="0 0 22 16" aria-hidden="true">
          <rect x="1" y="1" width="20" height="14" fill="none" stroke="#fff" stroke-width="1.6"/>
          <polyline points="1,1 11,9 21,1" fill="none" stroke="#fff" stroke-width="1.6"/>
        </svg>
        @EMAIL
      </span>
      <span class="contact">
        <svg width="18" height="18" viewBox="0 0 18 18" aria-hidden="true">
          <path d="M4 1l3 4-2 2c1 2 3 4 5 5l2-2 4 3-2 3C8 16 2 10 1 4z" fill="#fff"/>
        </svg>
        555-555-5555
      </span>
      <span class="contact">
        <svg width="20" height="18" viewBox="0 0 20 18" aria-hidden="true">
          <rect x="5" y="1" width="10" height="6" fill="none" stroke="#fff" stroke-width="1.5"/>
          <rect x="1" y="6" width="18" height="11" rx="1.5" fill="#fff"/>
          <rect x="4" y="9" width="8" height="2" fill="#6498cf"/>
          <rect x="14" y="9" width="3" height="5" fill="#6498cf"/>
        </svg>
        555-555-5555
      </span>
    </div>
  </section>

</main>
</body>
</html>
```